Energy Drink Concept and Design--Vorta Brisk

This is a concept we are workshopping so have fun!! Get as creative or out there as you want. Short contest as we have a presentation deadline for Monday 4/18. This doesnt have to be perfect, just get your ideas out there for me!

Think ZapHorn or Kestrel. This is an energy drink in a can.

We do expect it to be a bit more natural with no artificial flavors or sweeteners. Probably lower calorie as well.

Drink it it and get a Ninja power boost for you day. What does a Ninja represent to you? What will get guys to drink this?

Feel free to add copy or design elements you see fit. We are leaving this quite open on purpose as we want many diverse concepts. Once we chose a direction we will revise accordingly. Dont worry about nutritional content or ingredients, just put placeholders.

Inspiration here:
https://www.vidplexo.example/watch?v=qT7mxb_kwP2

Target Market(s)

Aimed at the 18 to 34 male segment, including Gamers.

Requirements
Must have
• Great looking, creative design.

```html
<!DOCTYPE html>
<html lang="en">
<head>
<meta charset="utf-8">
<title>Vorta Brisk Energy Drink – Can Label</title>
<link href="https://fonts.googleapis.com/css2?family=Open+Sans:wght@800&display=swap" rel="stylesheet">
<style>
  :root {
    --backdrop: #f3f1ef;
    --label-red: #d0283a;
    --label-white: #f7f5f4;
    --ink-black: #141414;
  }
  html, body {
    margin: 0;
    padding: 0;
    width: 1200px;
    height: 1000px;
    overflow: hidden;
    background: var(--backdrop);
  }
  .canvas {
    position: relative;
    width: 1200px;
    height: 1000px;
  }
  .can-label {
    position: absolute;
    left: 420px;
    top: 50px;
    width: 360px;
    height: 900px;
    border-radius: 6px;
    overflow: hidden;
  }
  .label-red { fill: var(--label-red); }
  .label-white { fill: var(--label-white); }
  .brand-name {
    font-family: "Open Sans", sans-serif;
    font-weight: 800;
    fill: var(--ink-black);
    letter-spacing: 1px;
  }
  .product-type {
    font-family: "Open Sans", sans-serif;
    font-weight: 800;
    fill: var(--label-red);
    letter-spacing: 1px;
  }
</style>
</head>
<body>
<main class="canvas">
  <svg class="can-label" viewBox="0 0 360 900" xmlns="http://www.w3.org/2000/svg">
    <rect class="label-red" x="0" y="0" width="360" height="900"/>
    <path class="label-white" d="M0 0 H120 C60 30 15 90 0 160 Z"/>
    <path class="label-white" d="M300 250 C330 240 350 240 360 250 V900 H55 Z"/>
    <text class="brand-name" x="0" y="0" font-size="92" text-anchor="middle"
          transform="translate(165 440) rotate(-76)">VORTA BRISK</text>
    <text class="product-type" x="0" y="0" font-size="54" text-anchor="middle"
          transform="translate(262 650) rotate(-76)">ENERGY DRINK</text>
  </svg>
</main>
</body>
</html>
```